Web Design for ORV Air conditioning company

Hello,

I am calling on you for the modernization of the company's website
https://clim-solaris-atelier.fr/

The new one must include the new logo with the new graphic charter (color, style ...)

I'm looking for a simple design (less is more), a font written without Serif, the logo that brings a touch of color and modernity.

(maintenance and installation company for air conditioning and ventilation systems)
COLORS: in line with the logo

CHAPTER:

# PRESENTATION
# SERVICES
AIR CONDITIONING (ice cube icon)
HEATING (flame icon)
AIR TREATMENT (icon fan)
# ACHIEVEMENTS

# CONTACT
CONTACT FORM
GOOGLE MAPS

Target Market(s)

Showcase site for our customers

Coding

Coded - Design and coding required

Number of Pages Required

4 page

Font styles to use
Sans Serif

Colors
33b8a4
33a6d7
3176b5
ffffff

Requirements
Must have
• Clear and fluid navigation
a visual identity of the page with the logo
Should not have
• Overloaded.

```html
<!DOCTYPE html>
<html lang="en">
<head>
<meta charset="utf-8">
<title>ORV – Air conditioning &amp; maintenance</title>
<link href="https://fonts.googleapis.com/css2?family=Josefin+Sans:wght@400;600;700&family=Lato:ital,wght@0,400;0,700;1,400&display=swap" rel="stylesheet">
<style>
:root{
  --teal:#33b8a4;
  --sky:#33a6d7;
  --blue:#3176b5;
  --white:#ffffff;
  --ink:#2b3a44;
  --slate:#2f3e49;
  --slate-2:#3d4f5c;
  --text:#5b6670;
  --line:#d9dee2;
  --footer:#2a2a2a;
  --footer-2:#1f1f1f;
}
*{box-sizing:border-box;margin:0;padding:0}
html,body{width:1200px;height:4208px;overflow:hidden;background:var(--white)}
body{font-family:"Lato",sans-serif;color:var(--text);position:relative}
.page{position:relative;width:1200px;height:4208px;overflow:hidden}
.abs{position:absolute}
h1,h2,h3,.display{font-family:"Josefin Sans",sans-serif;color:var(--ink);font-weight:600}
p{font-size:11.5px;line-height:26px}

/* top bar */
.topbar{top:0;left:0;width:1200px;height:38px;border-bottom:1px solid var(--line);font-size:11px;color:#8b949b}
.topbar .item{position:absolute;top:0;height:38px;display:flex;align-items:center;gap:12px;padding:0 30px 0 0}
.topbar .sep{position:absolute;top:0;width:1px;height:38px;background:var(--line)}
.social{display:flex;gap:0}
.social span{width:36px;height:38px;display:flex;align-items:center;justify-content:center}
.social i{width:12px;height:12px;border-radius:50%;background:#7d8a94;display:block}
.social span.on{background:var(--sky)}
.social span.on i{background:var(--white)}

/* header */
.header{top:38px;left:0;width:1200px;height:92px;border-bottom:3px solid var(--teal)}
.brand{position:absolute;left:111px;top:20px;display:flex;align-items:center;gap:14px}
.brand .mark{font-family:"Josefin Sans",sans-serif;font-weight:700;font-size:44px;color:var(--ink);letter-spacing:2px;line-height:1}
.brand .tag{font-size:11px;font-weight:700;color:var(--teal);letter-spacing:.3px;margin-top:14px}
.nav{position:absolute;right:110px;top:52px;display:flex;gap:38px;font-size:11px;color:var(--ink);letter-spacing:.3px}

/* hero */
.hero{top:130px;left:0;width:1200px;height:569px;background:linear-gradient(100deg,#e8eef3 0%,#dfe7ee 40%,#cfd9e2 70%,#bfcad4 100%)}
.hero-card{top:302px;left:573px;width:537px;height:248px;background:rgba(62,78,90,.88);padding:52px 26px 0 26px;color:var(--white)}
.hero-card h1{color:var(--white);font-size:29px;font-weight:600;letter-spacing:.3px}
.hero-card .sub{font-family:"Josefin Sans",sans-serif;font-size:17px;margin-top:14px}
.btn{display:inline-flex;align-items:center;justify-content:center;font-size:11px;height:38px;padding:0 26px;letter-spacing:.3px}
.btn-solid{background:var(--teal);color:var(--white)}
.btn-ghost{border:2px solid var(--sky);color:var(--white)}
.btn-line{border:2px solid var(--teal);color:var(--ink);background:var(--white)}
.hero-card .actions{display:flex;gap:14px;margin-top:22px}

/* features */
.features{top:640px;left:124px;width:951px;height:140px;background:var(--white);box-shadow:0 6px 18px rgba(0,0,0,.15);padding:5px}
.features .inner{border:3px solid var(--teal);height:100%;display:flex;padding:24px 0 0 30px}
.feature{width:314px;display:flex;gap:24px}
.feature h3{font-size:14px;font-family:"Lato",sans-serif;font-weight:700;color:var(--ink);margin-bottom:6px}
.feature p{font-size:10.5px;line-height:18px;width:170px}

/* who */
.who-photo{top:895px;left:114px;width:443px;height:374px;background:linear-gradient(120deg,#cfd4d8,#e6e9ec 50%,#9fb4c6)}
.badge{top:1163px;left:433px;width:163px;height:168px;background:linear-gradient(135deg,var(--sky),var(--blue));padding:6px}
.badge .in{background:var(--white);height:100%;text-align:center;padding-top:20px}
.badge .num{font-family:"Josefin Sans",sans-serif;font-weight:700;font-size:70px;color:var(--blue);line-height:1}
.badge .lbl{font-family:"Josefin Sans",sans-serif;font-size:17px;color:var(--sky);line-height:22px}
.badge .lbl b{color:#e0a96a;font-weight:400}
.who-text{top:910px;left:647px;width:440px}
.who-text h2{font-size:33px;margin-bottom:26px}
.who-text p{font-size:11px;line-height:26px;margin-bottom:24px}

/* services */
.services{top:1413px;left:0;width:1200px;height:669px;background:var(--slate)}
.services h2{position:absolute;top:68px;width:100%;text-align:center;color:var(--white);font-size:33px}
.svc{position:absolute;top:150px;width:312px;height:424px;background:var(--white);border:2px solid #c9d6de;text-align:center;padding-top:26px}
.svc h3{font-size:20px;margin-top:38px}
.svc p{font-size:11px;line-height:26px;width:250px;margin:18px auto 0}
.svc .btn{margin-top:46px;height:38px}

/* stats */
.stats{top:2082px;left:0;width:1200px;height:196px;background:linear-gradient(90deg,#4fb895 0%,#33b3a8 35%,#2fa3b8 70%,#2f93c8 100%)}
.stat{position:absolute;top:21px;width:230px;height:146px;border:2px solid rgba(255,255,255,.35);text-align:center;color:var(--white);padding-top:20px}
.stat .n{font-family:"Josefin Sans",sans-serif;font-weight:600;font-size:58px;line-height:1.1}
.stat .l{font-size:19px;font-weight:700;letter-spacing:.3px}

/* spirit */
.kicker{top:2375px;left:108px;font-family:"Josefin Sans",sans-serif;font-weight:600;font-size:20px;color:var(--teal)}
.spirit-title{top:2408px;left:106px;font-size:35px;line-height:44px;width:470px}
.spirit-text{top:2512px;left:111px;width:440px}
.spirit-text p{font-size:11px;line-height:26px}
.checks{list-style:none;margin-top:2px}
.checks li{display:flex;align-items:center;gap:12px;font-size:11px;height:26px}
.spirit-btn{top:2770px;left:113px}
.photo-big{top:2371px;left:665px;width:535px;height:482px;background:linear-gradient(135deg,#e9ecee,#b9c0c6 45%,#c9503a 80%,#d8dcdf)}
.photo-small{top:2572px;left:563px;width:319px;height:237px;background:linear-gradient(120deg,#d6dce2,#eef0f2 50%,#4f6f93);border:3px solid var(--white)}

/* reviews */
.reviews{top:2940px;left:0;width:1200px;height:411px;background:linear-gradient(90deg,#3f5462,#4a6070 50%,#3f5563)}
.reviews h2{position:absolute;top:72px;width:100%;text-align:center;color:var(--white);font-size:33px}
.reviews .quote{position:absolute;top:130px;left:200px;width:800px;text-align:center;color:var(--white);font-size:11px;line-height:26px}
.reviews .qm{font-family:"Josefin Sans",sans-serif;font-size:30px;color:var(--white);position:absolute}
.reviews .who{position:absolute;top:230px;width:100%;text-align:center;color:var(--white);font-family:"Josefin Sans",sans-serif;font-weight:600;font-size:19px}
.reviews .stars{position:absolute;top:262px;width:100%;text-align:center;color:#f2c94c;font-size:15px;letter-spacing:2px}
.dots{position:absolute;top:358px;left:574px;display:flex;gap:6px}
.dots i{width:6px;height:6px;background:var(--white);display:block}
.dots i.on{background:var(--teal)}

/* contact */
.contact h2{position:absolute;top:3438px;width:1200px;text-align:center;font-size:33px}
.field{position:absolute;border:1px solid #cfd5da;font-size:10px;font-style:italic;color:#a7afb5;padding:10px 12px}
.submit{top:3669px;left:539px;width:122px;height:38px;border:2px solid var(--teal);font-size:11px;color:var(--ink);display:flex;align-items:center;justify-content:center}

/* footer */
.footer{top:3785px;left:0;width:1200px;height:363px;background:var(--footer);color:#d7d7d7}
.footer .logo{position:absolute;left:111px;top:70px;font-family:"Josefin Sans",sans-serif;font-weight:700;font-size:58px;color:var(--white);letter-spacing:3px;line-height:1}
.footer p{font-size:11px;line-height:26px;color:#d7d7d7}
.footer h4{position:absolute;top:103px;font-family:"Josefin Sans",sans-serif;font-weight:600;font-size:20px;color:var(--white)}
.footer .col{position:absolute;top:157px}
.footer .links{list-style:none;font-size:11px;line-height:26px}
.footer .info{list-style:none;font-size:11px;line-height:26px}
.footer .info li{display:flex;align-items:center;gap:8px}
.map{position:absolute;left:834px;top:162px;width:254px;height:139px;background:linear-gradient(135deg,#eef0f2,#e4e8ec 60%,#dfe6ea);border:1px solid #ccc}
.bottom{top:4148px;left:0;width:1200px;height:60px;background:var(--footer-2);color:#e0e0e0;font-size:11px}
.bottom .copy{position:absolute;left:111px;top:23px}
.bottom .soc{position:absolute;right:110px;top:24px;display:flex;gap:24px}
.bottom .soc i{width:11px;height:11px;border-radius:50%;background:#e0e0e0;display:block}
</style>
</head>
<body>
<div class="page">

  <!-- top bar -->
  <div class="abs topbar">
    <div class="item" style="left:111px">
      <svg width="18" height="13" viewBox="0 0 18 13"><rect x="1" y="1" width="16" height="11" fill="none" stroke="#33b8a4" stroke-width="1.5"/><path d="M1 1l8 6 8-6" fill="none" stroke="#33b8a4" stroke-width="1.5"/></svg>
      <span>contact@orv-clim.fr</span>
    </div>
    <div class="sep" style="left:330px"></div>
    <div class="item" style="left:360px">
      <svg width="16" height="16" viewBox="0 0 16 16"><path d="M3 1l3 3-1.6 2.2c.9 2 2.4 3.5 4.4 4.4L11 9l3 3-2 3C6 14 2 10 1 3z" fill="#33b8a4"/></svg>
      <span>TEL: 04 76 10 20 30</span>
    </div>
    <div class="sep" style="left:527px"></div>
    <div class="social" style="position:absolute;left:880px;top:0">
      <span class="on"><i></i></span><span><i></i></span><span><i></i></span><span><i></i></span><span><i></i></span><span><i></i></span>
    </div>
  </div>

  <!-- header -->
  <header class="abs header">
    <div class="brand"><span class="mark">ORV</span><span class="tag">ORV CLIM SERVICES</span></div>
    <nav class="nav"><span>HOME</span><span>WHO WE ARE?</span><span>OUR SERVICES</span><span>CONTACT US</span></nav>
  </header>

  <!-- hero -->
  <section class="abs hero" role="img" aria-label="Smiling technician opening the cover of a wall-mounted air conditioning unit"></section>
  <div class="abs hero-card">
    <h1>ORV CLIMATE SERVICES</h1>
    <div class="sub">THE SOLUTION TO YOUR MAINTENANCE PROBLEM</div>
    <div class="actions"><span class="btn btn-solid">CONTACT US</span><span class="btn btn-ghost">READ MORE</span></div>
  </div>

  <!-- features -->
  <div class="abs features"><div class="inner">
    <div class="feature">
      <svg width="56" height="56" viewBox="0 0 56 56"><path d="M10 46L38 18" stroke="#33b8a4" stroke-width="6" stroke-linecap="round"/><circle cx="42" cy="14" r="8" fill="none" stroke="#33a6d7" stroke-width="5"/><path d="M12 12l32 32" stroke="#3176b5" stroke-width="5" stroke-linecap="round"/><path d="M8 8l6 2 -4 4z" fill="#3176b5"/></svg>
      <div><h3>INSTALLATION</h3><p>Lorem Ipsum is simply dummy text of the printing and typesetting industry.</p></div>
    </div>
    <div class="feature">
      <svg width="56" height="56" viewBox="0 0 56 56"><circle cx="22" cy="22" r="14" fill="none" stroke="#33b8a4" stroke-width="6" stroke-dasharray="6 3"/><circle cx="22" cy="22" r="5" fill="#33a6d7"/><path d="M32 32l16 16" stroke="#3176b5" stroke-width="6" stroke-linecap="round"/></svg>
      <div><h3>MAINTENANCE</h3><p>Lorem Ipsum is simply dummy text of the printing and typesetting industry.</p></div>
    </div>
    <div class="feature">
      <svg width="56" height="56" viewBox="0 0 56 56"><circle cx="24" cy="24" r="16" fill="#33b8a4"/><circle cx="24" cy="24" r="9" fill="#fff"/><path d="M35 35l13 13" stroke="#3176b5" stroke-width="6" stroke-linecap="round"/></svg>
      <div><h3>TROUBLESHOOTING</h3><p>Lorem Ipsum is simply dummy text of the printing and typesetting industry.</p></div>
    </div>
  </div></div>

  <!-- who we are -->
  <div class="abs who-photo" role="img" aria-label="Technician in a blue cap checking an outdoor air conditioning unit with pressure gauges"></div>
  <div class="abs badge"><div class="in"><div class="num">25</div><div class="lbl">YEAR <b>OF</b><br><b>EXPERIENCE</b></div></div></div>
  <div class="abs who-text">
    <h2>WHO WE ARE?</h2>
    <p>Lorem Ipsum is simply dummy text of the printing and typesetting industry. Lorem Ipsum has been the industry's standard dummy text ever since the 1500s, when an unknown printer took a galley of type and scrambled it to make a type specimen book. It has survived not only five centuries, but also the leap into electronic typesetting, remaining essentially unchanged.</p>
    <p>It was popularised in the 1960s with the release of Letraset sheets containing Lorem Ipsum passages, and more recently with desktop publishing software like Aldus PageMaker including versions of Lorem Ipsum.</p>
    <span class="btn btn-line">READ MORE</span>
  </div>

  <!-- services -->
  <section class="abs services">
    <h2>OUR SERVICES</h2>
    <div class="svc" style="left:111px">
      <svg width="80" height="76" viewBox="0 0 80 76"><path d="M8 22L34 10l26 12v30L34 66 8 52z" fill="#33b8a4"/><path d="M8 22l26 12 26-12" fill="none" stroke="#2a9c8a" stroke-width="2"/><path d="M34 34v32" stroke="#2a9c8a" stroke-width="2"/><path d="M56 54c6 0 14 4 18 8H44z" fill="#33a6d7"/></svg>
      <h3>AIR CONDITIONING</h3>
      <p>Lorem Ipsum is simply dummy text of the printing and typesetting industry. Lorem Ipsum has been the industry's standard dummy text ever since the 1500s,.</p>
      <span class="btn btn-line">READ MORE</span>
    </div>
    <div class="svc" style="left:443px">
      <svg width="80" height="76" viewBox="0 0 80 76"><path d="M40 4c4 14 20 22 20 42a20 20 0 0 1-40 0c0-10 6-16 8-22 2 8 6 10 6 10 0-14 4-22 6-30z" fill="#33b8a4"/><path d="M40 40c3 6 9 10 9 18a9 9 0 0 1-18 0c0-6 6-10 9-18z" fill="#33a6d7"/></svg>
      <h3>HEATING</h3>
      <p>Lorem Ipsum is simply dummy text of the printing and typesetting industry. Lorem Ipsum has been the industry's standard dummy text ever since the 1500s,.</p>
      <span class="btn btn-line">READ MORE</span>
    </div>
    <div class="svc" style="left:773px">
      <svg width="80" height="76" viewBox="0 0 80 76"><rect x="10" y="4" width="62" height="62" rx="4" fill="none" stroke="#33b8a4" stroke-width="4"/><circle cx="41" cy="35" r="22" fill="none" stroke="#33a6d7" stroke-width="3"/><g stroke="#33b8a4" stroke-width="4" stroke-linecap="round"><path d="M41 35l-6-16"/><path d="M41 35l16-6"/><path d="M41 35l6 16"/><path d="M41 35l-16 6"/></g><circle cx="41" cy="35" r="4" fill="#3176b5"/></svg>
      <h3>AIR TREATMENT</h3>
      <p>Lorem Ipsum is simply dummy text of the printing and typesetting industry. Lorem Ipsum has been the industry's standard dummy text ever since the 1500s,.</p>
      <span class="btn btn-line">READ MORE</span>
    </div>
  </section>

  <!-- stats -->
  <section class="abs stats">
    <div class="stat" style="left:111px"><div class="n">7</div><div class="l">CLIENTS</div></div>
    <div class="stat" style="left:360px"><div class="n">650</div><div class="l">CONTRACT</div></div>
    <div class="stat" style="left:609px"><div class="n">590</div><div class="l">SATISFIED</div></div>
    <div class="stat" style="left:857px"><div class="n">1752</div><div class="l">STOCK PRODUCTS</div></div>
  </section>

  <!-- spirit of service -->
  <div class="abs kicker">THE SPIRIT OF SERVICE</div>
  <h2 class="abs spirit-title">MAINTENANCE OF WATER TREATMENT SYSTEM</h2>
  <div class="abs spirit-text">
    <p>Lorem Ipsum is simply dummy text of the printing and typesetting industry. Lorem Ipsum has been the industry's standard dummy text ever since the 1500s.</p>
    <ul class="checks">
      <li><svg width="16" height="14" viewBox="0 0 16 14"><path d="M1 7l5 5L15 1" fill="none" stroke="#33b8a4" stroke-width="3"/></svg>Soft water</li>
      <li><svg width="16" height="14" viewBox="0 0 16 14"><path d="M1 7l5 5L15 1" fill="none" stroke="#33b8a4" stroke-width="3"/></svg>Osmotic water</li>
      <li><svg width="16" height="14" viewBox="0 0 16 14"><path d="M1 7l5 5L15 1" fill="none" stroke="#33b8a4" stroke-width="3"/></svg>maintenance of softeners</li>
      <li><svg width="16" height="14" viewBox="0 0 16 14"><path d="M1 7l5 5L15 1" fill="none" stroke="#33b8a4" stroke-width="3"/></svg>treatment of liquid effluents</li>
      <li><svg width="16" height="14" viewBox="0 0 16 14"><path d="M1 7l5 5L15 1" fill="none" stroke="#33b8a4" stroke-width="3"/></svg>Calibration of pH probes</li>
      <li><svg width="16" height="14" viewBox="0 0 16 14"><path d="M1 7l5 5L15 1" fill="none" stroke="#33b8a4" stroke-width="3"/></svg>Conductivity probe calibration</li>
      <li><svg width="16" height="14" viewBox="0 0 16 14"><path d="M1 7l5 5L15 1" fill="none" stroke="#33b8a4" stroke-width="3"/></svg>Analog level management</li>
    </ul>
  </div>
  <span class="abs btn btn-line spirit-btn">CONTACT US</span>
  <div class="abs photo-big" role="img" aria-label="Hands connecting wiring and copper pipes inside an open air conditioning unit"></div>
  <div class="abs photo-small" role="img" aria-label="Technician servicing an outdoor condenser unit with a gauge manifold"></div>

  <!-- reviews -->
  <section class="abs reviews" role="region" aria-label="Client reviews">
    <h2>CLIENT`S REVIEWS</h2>
    <span class="qm" style="left:180px;top:120px">&ldquo;</span>
    <p class="quote">Lorem Ipsum is simply dummy text of the printing and typesetting industry. Lorem Ipsum has been the industry's standard dummy text ever since the 1500s, when an unknown printer took a galley of type and scrambled it to make a type specimen book. It has survived not only five centuries, but also the leap into electronic typesetting, remaining essentially unchanged.</p>
    <span class="qm" style="left:806px;top:178px">&rdquo;</span>
    <div class="who">JULIAN</div>
    <div class="stars">★★★★★</div>
    <div class="dots"><i class="on"></i><i></i><i></i><i></i></div>
  </section>

  <!-- contact -->
  <section class="contact">
    <h2>CONTACT US</h2>
    <div class="field" style="left:312px;top:3506px;width:281px;height:38px">Full Name</div>
    <div class="field" style="left:312px;top:3555px;width:281px;height:38px">Phone</div>
    <div class="field" style="left:312px;top:3604px;width:281px;height:38px">Email</div>
    <div class="field" style="left:604px;top:3506px;width:280px;height:136px">Message</div>
    <div class="abs submit">SUBMIT NOW</div>
  </section>

  <!-- footer -->
  <footer class="abs footer">
    <div class="logo">ORV</div>
    <div class="col" style="left:111px;top:157px;width:240px">
      <p>Lorem Ipsum is simply dummy text of the printing and typesetting industry. Lorem Ipsum has been the industry's standard dummy text ever since the 1500s.</p>
      <p style="text-decoration:underline;margin-top:14px">READ MORE</p>
    </div>
    <h4 style="left:403px">QUICK LINKS</h4>
    <ul class="col links" style="left:410px"><li>Home</li><li>Who we are?</li><li>Our Services</li><li>Contact us</li></ul>
    <h4 style="left:580px">CONTACT INFO</h4>
    <ul class="col info" style="left:568px">
      <li><svg width="10" height="12" viewBox="0 0 10 12"><path d="M5 0a4 4 0 0 1 4 4c0 3-4 8-4 8S1 7 1 4a4 4 0 0 1 4-4z" fill="#33b8a4"/></svg>12 Rue des Tilleuls</li>
      <li style="padding-left:18px">38000 VAL DES PINS</li>
      <li>&nbsp;</li>
      <li><svg width="10" height="10" viewBox="0 0 16 16"><path d="M3 1l3 3-1.6 2.2c.9 2 2.4 3.5 4.4 4.4L11 9l3 3-2 3C6 14 2 10 1 3z" fill="#33b8a4"/></svg>Tel: 04 76 10 20 30</li>
      <li><svg width="10" height="10" viewBox="0 0 10 10"><rect x="1" y="3" width="8" height="6" fill="#33b8a4"/><rect x="3" y="0" width="4" height="3" fill="#33b8a4"/></svg>Fax: 04 76 10 20 31</li>
      <li><svg width="10" height="8" viewBox="0 0 18 13"><rect x="1" y="1" width="16" height="11" fill="#33b8a4"/></svg>contact@orv-clim.fr</li>
    </ul>
    <h4 style="left:832px">LOCATION MAP</h4>
    <div class="map" role="img" aria-label="Street map showing the company location"></div>
  </footer>
  <div class="abs bottom">
    <span class="copy">Copyright © 2020 Orv Clim Services. All Right Resserved.</span>
    <div class="soc"><i></i><i></i><i></i><i></i><i></i><i></i></div>
  </div>

</div>
</body>
</html>
```